Vertical retractable banner/pop-up for conference

We need a banner for a personal tax business based in Luxembourg to use at conferences/presentations etc.

The company name is Morvane Tax & Consulting - please view the website www.morvanetax.example for the style of our business and use of colours.

The colours we use are:-
#7D1935
#4A96AD
#F5F3EE

Also uploaded are the logo files and the template from the printing company to ensure that the sizes/margins are correct.

Requirements
Must have
• Use of corporate colours (see above).
• Logo
• Website address
Nice to have
• We are open to ideas on style so do not want to prescribe too much as we would like to receive a variety of possible designs ranging from the more minimalist options to more detailed. Some considerations for the design could be to use:-
• 1) The tagline from the website - "Specialists in personal and expatriate taxation".
• 2) The website background is a picture of Luxembourg - if similar city pictures are used on the banner then they should be of Luxembourg also (i.e. not other cities).

```html
<!DOCTYPE html>
<html lang="en">
<head>
<meta charset="utf-8">
<title>Morvane Tax &amp; Consulting – Conference Roll-up Banner</title>
<link rel="stylesheet" href="https://fonts.googleapis.com/css2?family=Open+Sans:wght@600;700&display=swap">
<style>
  :root {
    --brand-maroon: #7D1935;
    --brand-teal: #4A96AD;
    --brand-cream: #F5F3EE;
    --panel-grey: #ededed;
    --text-grey: #6b6b6b;
    --page-bg: #f4f4f4;
    --photo-light: #d9d9d9;
    --photo-mid: #9a9a9a;
    --photo-dark: #5e5e5e;
  }
  * { box-sizing: border-box; margin: 0; padding: 0; }
  html, body {
    width: 1200px;
    height: 1000px;
    overflow: hidden;
    background: var(--page-bg);
    font-family: "Open Sans", Arial, sans-serif;
  }
  .canvas {
    position: relative;
    width: 1200px;
    height: 1000px;
  }
  .rollup-banner {
    position: absolute;
    left: 403px;
    top: 42px;
    width: 394px;
    height: 916px;
    background: var(--panel-grey);
    overflow: hidden;
  }
  .brand-lockup {
    position: absolute;
    top: 78px;
    left: 0;
    width: 100%;
    display: flex;
    align-items: center;
    justify-content: center;
    gap: 16px;
  }
  .brand-mark {
    width: 70px;
    height: 70px;
    flex: none;
  }
  .brand-name {
    color: var(--brand-maroon);
    font-weight: 600;
    line-height: 1.05;
  }
  .brand-name .brand-primary {
    display: block;
    font-size: 44px;
    letter-spacing: 1px;
  }
  .brand-name .brand-secondary {
    display: block;
    font-size: 19px;
    letter-spacing: 0.5px;
  }
  .service-statement {
    position: absolute;
    top: 246px;
    left: 0;
    width: 100%;
    text-align: center;
    font-weight: 700;
  }
  .service-statement .headline {
    display: block;
    color: var(--brand-maroon);
    font-size: 30px;
    letter-spacing: 2px;
    line-height: 40px;
  }
  .service-statement .subline {
    display: block;
    color: var(--text-grey);
    font-size: 23px;
    letter-spacing: 1px;
    line-height: 30px;
    margin-bottom: 12px;
  }
  .city-photo {
    position: absolute;
    left: 0;
    top: 400px;
    width: 100%;
    height: 516px;
    background: linear-gradient(180deg,
      var(--panel-grey) 0%,
      var(--photo-light) 12%,
      var(--photo-mid) 35%,
      var(--photo-dark) 60%,
      var(--photo-mid) 80%,
      var(--photo-light) 100%);
  }
  .web-band {
    position: absolute;
    left: 0;
    top: 770px;
    width: 100%;
    height: 61px;
    background: var(--brand-maroon);
    color: #ffffff;
    display: flex;
    align-items: center;
    justify-content: center;
    font-weight: 700;
    font-size: 23px;
    letter-spacing: 1.5px;
  }
</style>
</head>
<body>
  <div class="canvas">
    <section class="rollup-banner">
      <div class="brand-lockup">
        <svg class="brand-mark" viewBox="0 0 70 70" aria-hidden="true">
          <circle cx="35" cy="35" r="32" fill="none" stroke="var(--brand-maroon)" stroke-width="3"/>
        </svg>
        <div class="brand-name">
          <span class="brand-primary">MORVANE</span>
          <span class="brand-secondary">TAX &amp; CONSULTING</span>
        </div>
      </div>

      <p class="service-statement">
        <span class="headline">SPECIALISTS IN</span>
        <span class="subline">Luxembourg, UK and US</span>
        <span class="headline">PERSONAL TAX</span>
        <span class="subline">compliance and consulting</span>
      </p>

      <div class="city-photo" role="img" aria-label="Black and white photograph of Luxembourg old town: hilltop buildings and towers above fortress walls, with rooftops below"></div>

      <div class="web-band">WWW.MORVANETAX.EXAMPLE</div>
    </section>
  </div>
</body>
</html>
```